Yoga Instrucor

I need my personal business cards, i would like the front a kind of light but vibrant red and matt gold.

Industry/Entity Type

Business

Contact Information for Business Card

Rosalind Quenneby
Yoga Instructor
RYT 200, PRAVO (NYC) Yoga RYT 500,
CPR/ AED Certified,
quennebyrosalind@mailvista.net
512 804 6193
Adult Yoga, Private Yoga, Group Classes, Restorative, Meditation, Child Yoga.

```html
<!DOCTYPE html>
<html lang="en">
<head>
<meta charset="utf-8">
<title>Rosalind Quenneby – Yoga Instructor</title>
<link href="https://fonts.googleapis.com/css2?family=Kalam:wght@400;700&family=Tinos:wght@700&display=swap" rel="stylesheet">
<style>
  :root {
    --card-red: #ff0016;
    --figure-red: #ee0a16;
    --figure-red-deep: #e20814;
    --matt-gold: #f2a41e;
  }
  html, body {
    margin: 0;
    padding: 0;
    overflow: hidden;
    background: var(--card-red);
  }
  .card {
    position: relative;
    width: 1200px;
    height: 702px;
    background: var(--card-red);
    overflow: hidden;
    color: var(--matt-gold);
    font-family: "Kalam", cursive;
  }
  .figure {
    position: absolute;
    border-radius: 40px;
  }
  .figure--standing {
    left: 112px;
    top: 0;
    width: 264px;
    height: 702px;
    background: linear-gradient(180deg, var(--figure-red) 0%, var(--figure-red-deep) 100%);
  }
  .figure--seated {
    left: 719px;
    top: 243px;
    width: 420px;
    height: 354px;
    background: linear-gradient(160deg, var(--figure-red) 0%, var(--figure-red-deep) 100%);
  }
  .name {
    position: absolute;
    left: 0;
    width: 1228px;
    top: 48px;
    margin: 0;
    text-align: center;
    font-weight: 400;
    font-size: 56px;
    line-height: 1;
    letter-spacing: 1px;
  }
  .name-rule {
    position: absolute;
    left: 437px;
    top: 130px;
  }
  .role {
    position: absolute;
    left: 0;
    width: 1216px;
    top: 142px;
    margin: 0;
    text-align: center;
    font-size: 29px;
    line-height: 1;
  }
  .services {
    position: absolute;
    left: 0;
    top: 220px;
    width: 1216px;
    margin: 0;
    padding: 0;
    list-style: none;
    text-align: center;
    font-size: 42px;
    font-weight: 700;
    line-height: 55.3px;
  }
  .credentials {
    position: absolute;
    left: 0;
    width: 1228px;
    top: 598px;
    margin: 0;
    text-align: center;
    font-family: "Tinos", serif;
    font-weight: 700;
    font-size: 29px;
    line-height: 1;
  }
</style>
</head>
<body>
  <main class="card">
    <div class="figure figure--standing" role="img" aria-label="Line drawing of a woman standing in tree pose with arms raised overhead"></div>
    <div class="figure figure--seated" role="img" aria-label="Line drawing of a woman seated on the floor with legs stretched forward"></div>

    <h1 class="name">Rosalind Quenneby</h1>
    <svg class="name-rule" width="354" height="8" viewBox="0 0 354 8" aria-hidden="true">
      <path d="M2 5 Q177 1 352 3" stroke="var(--matt-gold)" stroke-width="4" fill="none" stroke-linecap="round"/>
    </svg>
    <p class="role">yoga instructor</p>

    <ul class="services">
      <li>Adult Yoga</li>
      <li>Private Yoga</li>
      <li>Group Classes</li>
      <li>Restorative</li>
      <li>Meditation</li>
      <li>Child Yoga</li>
    </ul>

    <p class="credentials">RYT 200, PRAVO (NYC) Yoga RYT 500, CPR/ AED Certified</p>
  </main>
</body>
</html>
```